IT Business Card Design

My company is a newly started small IT repair business. I operate outside of usual hours except for Saturday.
I am a very experienced and professional Technician.
I would like the business card to express that I am running a professional business and not some home IT business. This should be expressed through the design of the business card.
On the back of the card I would like the name of the company to be displayed.
Updates
Sorry guys, I have updated the requirement to be double sided. Fantastic submissions so far! Keep up the good work.
Hey designers!
Hey Designers!
Thank you all for your hard work!
Target Market(s)
Home to small business users.
Industry/Entity Type
Business
Contact Information for Business Card
Harbourlight Technics
Marcus Pendleby (Director)
marcus.pendleby@quorvanet.com.au
Operating Hours
5pm-12am Mon - Fri
9am - 5pm Sat
Mobile
0417962351
Requirements
Must have
- The base colour must be matte black. There must be some dark purple. (To go with the "Harbourlight" theme)

```html
<!DOCTYPE html>
<html lang="en">
<head>
<meta charset="utf-8">
<title>Harbourlight Technics – Business Card</title>
<link href="https://fonts.googleapis.com/css2?family=Orbitron:wght@500&family=Exo+2:wght@400;500&family=Open+Sans:wght@400&display=swap" rel="stylesheet">
<style>
  :root {
    --page-bg: #c9c9c9;
    --card-black: #1f1e1f;
    --brand-purple: #a9508f;
    --title-purple: #b2569a;
    --tab-grey: #3a393a;
    --text-white: #f4f4f4;
  }
  * { box-sizing: border-box; margin: 0; padding: 0; }
  html, body {
    width: 1200px; height: 894px; overflow: hidden;
    background: var(--page-bg);
  }
  .sheet {
    position: relative; width: 1200px; height: 894px;
    display: flex; flex-direction: column; align-items: center; justify-content: center; gap: 40px;
  }
  .card {
    position: relative; width: 720px; height: 411px;
    background: var(--card-black); overflow: hidden;
    box-shadow: 0 6px 18px rgba(0,0,0,0.25);
  }
  .card__band {
    position: absolute; left: 0; right: 0; bottom: 0; height: 78px;
    background: var(--brand-purple);
  }
  .card__frame {
    position: absolute; left: 30px; top: 24px; right: 30px; bottom: 52px;
    border: 3px solid var(--brand-purple);
  }
  .brand-name {
    font-family: "Orbitron", sans-serif; font-weight: 500;
    color: var(--title-purple); letter-spacing: 3px; line-height: 1.15;
    text-transform: uppercase;
  }
  .brand-name .initial { font-size: 1.25em; }

  /* back */
  .card--back .brand-name {
    position: absolute; left: 0; right: 0; top: 118px; text-align: center;
    font-size: 30px;
  }
  .card--back .web {
    position: absolute; left: 0; right: 0; bottom: 20px; text-align: center;
    font-family: "Open Sans", sans-serif; font-size: 21px; letter-spacing: 1px;
    color: var(--text-white);
  }

  /* front */
  .card--front .card__tab {
    position: absolute; left: 0; bottom: 0; width: 150px; height: 78px;
  }
  .card--front .brand-name {
    position: absolute; left: 62px; top: 52px; font-size: 27px;
  }
  .contact {
    position: absolute; display: flex; flex-direction: column; gap: 12px;
    font-family: "Open Sans", sans-serif; font-size: 15px; color: var(--text-white);
  }
  .contact--left { left: 62px; top: 158px; }
  .contact--right { left: 392px; top: 238px; }
  .contact__row { display: flex; align-items: flex-start; gap: 12px; line-height: 1.3; }
  .icon {
    flex: none; width: 22px; height: 22px; border-radius: 4px;
    background: var(--brand-purple); display: flex; align-items: center; justify-content: center;
  }
  .icon svg { width: 14px; height: 14px; }
  .person {
    position: absolute; left: 430px; top: 160px;
    font-family: "Exo 2", sans-serif; color: var(--text-white);
  }
  .person__name { font-size: 25px; font-weight: 500; letter-spacing: 1px; }
  .person__role { font-size: 15px; margin-top: 2px; }
</style>
</head>
<body>
<main class="sheet">

  <section class="card card--back" aria-label="Card back">
    <div class="card__band"></div>
    <div class="card__frame"></div>
    <h1 class="brand-name"><span class="initial">H</span>arbourlight<br><span class="initial">T</span>echnics</h1>
    <p class="web">www.harbourlighttechnics.com</p>
  </section>

  <section class="card card--front" aria-label="Card front">
    <div class="card__band"></div>
    <svg class="card__tab" viewBox="0 0 150 78" aria-hidden="true">
      <polygon points="0,0 130,0 150,78 0,78" fill="var(--tab-grey)"/>
    </svg>
    <div class="card__frame"></div>
    <h2 class="brand-name"><span class="initial">H</span>arbourlight<br><span class="initial">T</span>echnics</h2>

    <div class="contact contact--left">
      <div class="contact__row">
        <span class="icon"><svg viewBox="0 0 24 24"><path fill="#fff" d="M6.6 10.8a15.1 15.1 0 0 0 6.6 6.6l2.2-2.2c.3-.3.7-.4 1-.2 1.1.4 2.3.6 3.6.6.6 0 1 .4 1 1V20c0 .6-.4 1-1 1A17 17 0 0 1 3 4c0-.6.4-1 1-1h3.5c.6 0 1 .4 1 1 0 1.3.2 2.5.6 3.6.1.3 0 .7-.2 1z"/></svg></span>
        <span>0417 962 351</span>
      </div>
      <div class="contact__row">
        <span class="icon"><svg viewBox="0 0 24 24"><rect x="3" y="5" width="18" height="14" rx="1" fill="#fff"/><path d="M3 6l9 7 9-7" fill="none" stroke="var(--brand-purple)" stroke-width="2"/></svg></span>
        <span>marcus.pendleby@quorvanet.com.au</span>
      </div>
    </div>

    <div class="person">
      <div class="person__name">Marcus Pendleby</div>
      <div class="person__role">Production engineer</div>
    </div>

    <div class="contact contact--right">
      <div class="contact__row">
        <span class="icon"><svg viewBox="0 0 24 24"><path fill="#fff" d="M12 2a7 7 0 0 0-7 7c0 5 7 13 7 13s7-8 7-13a7 7 0 0 0-7-7zm0 9.5A2.5 2.5 0 1 1 12 6.5a2.5 2.5 0 0 1 0 5z"/></svg></span>
        <span>14 Tidewater Lane, Level 3<br>Portside QLD</span>
      </div>
      <div class="contact__row">
        <span class="icon"><svg viewBox="0 0 24 24"><circle cx="12" cy="12" r="9" fill="none" stroke="#fff" stroke-width="2"/><circle cx="12" cy="12" r="5" fill="none" stroke="#fff" stroke-width="2"/><circle cx="12" cy="12" r="1.5" fill="#fff"/></svg></span>
        <span>www.harbourlighttechnics.com</span>
      </div>
    </div>
  </section>

</main>
</body>
</html>
```